Larkvale Advertising PowerPoint Design Project

We need PowerPoint slide templates for our Sales Media Kit at our re-branded company based in Canada called "Larkvale Advertising Network".

Looking for a look that clearly and powerfully portrays our unique and effective indoor advertising billboards in our network.

Our PetiPanels, GrandPanels and TitanFlags are strategically placed in high traffic areas of restaurants, pubs, nightclubs, fitness clubs, colleges and universities, and sports arenas.

Key features of our media is a captive audience and 100% gender specific.

You can visit our old website for info on the above three media products (plovercrest.ca)

Our Media Kits go out to small, medium business owners and advertising agenices.

Deliverables are:

1) Presentation cover slide with rich graphic content and space for content.
2) Presentation body slide with room for content 2 photos or logos. This slide should have the following:
a) No graphic in the text area
b) Space for page number at the bottom.
3) Photoshop (PSD) files for all graphic elements.
4) Font files for all fonts used.
Updates

Project Deadline Extended
Reason: Need more designs submitted.

We have uploaded our business card file.

Would like to incorporate the look, feel and colour of our business card to the power point template.

Target Market(s)

small business owners, marketing managers, media buyers and advertising agencies.

Industry/Entity Type

Advertising

Requirements
Must have
• We would like to see designs that:
- use the color scheme indicated by the attached logo design, perhaps expanding on it slightly.
- Look should be professional, smooth, and colourful.
-Must have a clean and modern feel that Ad Agencies would be impressed with.
-We have uploaded our business card file.

-Would like to incorporate the look, feel and colour of our business card to the power point template.

```html
<!DOCTYPE html>
<html lang="en">
<head>
<meta charset="utf-8">
<title>Larkvale Advertising Network – Cover Slide</title>
<link href="https://fonts.googleapis.com/css2?family=PT+Sans+Narrow:wght@400;700&display=swap" rel="stylesheet">
<style>
  :root {
    --page-bg: #ffffff;
    --swoosh: #e4e4e4;
    --swoosh-soft: #f1f1f1;
    --heading-blue: #4a7fc0;
    --brand-blue: #2a6cb8;
    --brand-grey: #767676;
    --body-grey: #8c8c8c;
    --footer-ink: #1a1a1a;
    --footer-line: #e2e2e2;
  }
  * { margin: 0; padding: 0; box-sizing: border-box; }
  html, body {
    width: 1200px;
    height: 900px;
    overflow: hidden;
    background: var(--page-bg);
  }
  .slide {
    position: relative;
    width: 1200px;
    height: 900px;
    overflow: hidden;
    background: radial-gradient(ellipse at 70% 30%, #ffffff 0%, #f6f6f6 60%, #efefef 100%);
    font-family: "PT Sans Narrow", "Arial Narrow", sans-serif;
  }
  .backdrop-curves {
    position: absolute;
    inset: 0;
    width: 1200px;
    height: 900px;
  }
  .slide-heading {
    position: absolute;
    left: 75px;
    top: 390px;
    font-size: 50px;
    font-weight: 700;
    color: var(--heading-blue);
    letter-spacing: 0.3px;
  }
  .brand-lockup {
    position: absolute;
    left: 640px;
    top: 330px;
    display: flex;
    align-items: center;
    gap: 24px;
  }
  .brand-square {
    width: 150px;
    height: 150px;
    background: var(--brand-grey);
  }
  .brand-name {
    font-size: 92px;
    font-weight: 700;
    color: var(--brand-blue);
    line-height: 1;
  }
  .slide-body {
    position: absolute;
    left: 88px;
    top: 596px;
    width: 990px;
    font-size: 20px;
    font-weight: 700;
    line-height: 33px;
    color: var(--body-grey);
  }
  .slide-footer {
    position: absolute;
    left: 0;
    top: 802px;
    width: 1200px;
    height: 98px;
    border-top: 2px solid var(--footer-line);
    background: linear-gradient(to bottom, #f7f7f7 0%, #ececec 100%);
  }
  .copyright {
    position: absolute;
    left: 57px;
    top: 842px;
    font-size: 25px;
    color: var(--footer-ink);
  }
</style>
</head>
<body>
<div class="slide">
  <svg class="backdrop-curves" viewBox="0 0 1200 900" aria-hidden="true">
    <defs>
      <linearGradient id="curveFade" x1="0" y1="0" x2="1" y2="0">
        <stop offset="0" stop-color="#ffffff" stop-opacity="0"/>
        <stop offset="0.5" stop-color="#dcdcdc" stop-opacity="0.8"/>
        <stop offset="1" stop-color="#ffffff" stop-opacity="0"/>
      </linearGradient>
    </defs>
    <path d="M0 60 C 300 220, 700 160, 1200 0" fill="none" stroke="url(#curveFade)" stroke-width="40" opacity="0.5"/>
    <path d="M0 200 C 350 120, 750 330, 1200 90" fill="none" stroke="url(#curveFade)" stroke-width="4"/>
    <path d="M100 0 C 500 260, 900 60, 1200 220" fill="none" stroke="url(#curveFade)" stroke-width="3"/>
    <path d="M600 900 C 800 650, 1000 500, 1200 380" fill="none" stroke="url(#curveFade)" stroke-width="60" opacity="0.35"/>
    <path d="M700 900 C 900 640, 1050 560, 1200 470" fill="none" stroke="url(#curveFade)" stroke-width="3"/>
    <path d="M0 520 C 200 470, 400 520, 620 440" fill="none" stroke="url(#curveFade)" stroke-width="2" opacity="0.6"/>
  </svg>

  <h1 class="slide-heading">Content Heading Here</h1>

  <div class="brand-lockup">
    <div class="brand-square"></div>
    <span class="brand-name">Larkvale</span>
  </div>

  <p class="slide-body">Lorem ipsum dolor sit&nbsp; Lorem ipsum dolor sit&nbsp; Lorem ipsum dolor sit&nbsp; Lorem ipsum dolor sit Lorem ipsum dolor sit&nbsp; Lorem ipsum dolor sit Lorem ipsum dolor sit&nbsp; Lorem ipsum dolor sit Lorem ipsum dolor sit&nbsp; Lorem ipsum dolor sit .</p>

  <div class="slide-footer"></div>
  <p class="copyright">Copyright@larkvale</p>
</div>
</body>
</html>
```